Lounge Bar Menu

We need an elegant Bar Menu for ou Lounge Bar.
Logo attached.
We already have the support. A cover like a book in A5 format.
Attached as well our menu.

Industry/Entity Type

Bar, Hotel4*

```html
<!DOCTYPE html>
<html lang="fr">
<head>
<meta charset="utf-8">
<title>Valmo – Carte du bar</title>
<link rel="stylesheet" href="https://fonts.googleapis.com/css2?family=Carlito:wght@400;700&family=Lobster+Two:ital,wght@1,700&display=swap">
<style>
  :root {
    --page: #ffffff;
    --black: #000000;
    --panel-black: #0a0a0a;
    --gold: #d4af3a;
    --ink: #1c1a14;
  }
  * { margin: 0; padding: 0; box-sizing: border-box; }
  html, body { width: 1200px; height: 1200px; overflow: hidden; background: var(--page); }
  body { position: relative; font-family: "Carlito", "Calibri", sans-serif; color: var(--ink); }

  /* ---------- Cover ---------- */
  .cover {
    position: absolute; left: 13px; top: 198px; width: 573px; height: 812px;
    background: var(--black);
  }
  .cover-band {
    position: absolute; left: 176px; top: 25px; width: 221px; height: 763px;
    background: var(--gold);
  }
  .cover-title {
    position: absolute; left: 0; width: 100%; top: 96px; text-align: center;
    font-family: "Lobster Two", cursive; font-style: italic; font-weight: 700;
    font-size: 44px; color: var(--black); letter-spacing: 1px;
  }
  .cover-rule {
    position: absolute; left: 7px; width: 207px; height: 2px; background: var(--black);
  }
  .cover-rule.top { top: 332px; }
  .cover-rule.bottom { top: 427px; }
  .cover-name {
    position: absolute; left: 0; width: 100%; top: 348px; text-align: center;
    font-family: "Carlito", sans-serif; font-weight: 400; font-size: 38px;
    letter-spacing: 14px; padding-left: 14px; color: var(--black);
  }

  /* ---------- Menu page ---------- */
  .menu-page {
    position: absolute; left: 617px; top: 198px; width: 572px; height: 812px;
    background: var(--panel-black);
  }
  .menu-page svg.frame { position: absolute; left: 0; top: 0; }
  .ornament {
    position: absolute; width: 56px; height: 56px; background: var(--gold);
    border-radius: 40% 40% 40% 40%;
  }
  .ornament.tl { left: 6px; top: 10px; border-radius: 0 0 60% 0; }
  .ornament.tr { right: 6px; top: 10px; border-radius: 0 0 0 60%; }
  .ornament.bl { left: 6px; bottom: 10px; border-radius: 0 60% 0 0; }
  .ornament.br { right: 6px; bottom: 10px; border-radius: 60% 0 0 0; }

  .brand-pill {
    position: absolute; left: 152px; top: 30px; width: 270px; height: 77px;
    border-radius: 39px; background: var(--gold);
    display: flex; align-items: center; justify-content: center;
    font-weight: 400; font-size: 34px; letter-spacing: 13px; padding-left: 13px;
    color: var(--black);
  }
  .page-title {
    position: absolute; left: 0; width: 100%; top: 118px; text-align: center;
    font-family: "Lobster Two", cursive; font-style: italic; font-weight: 700;
    font-size: 26px; color: var(--panel-black);
    -webkit-text-stroke: 1.2px var(--gold);
  }
  .carte-title {
    position: absolute; left: 0; width: 100%; top: 183px; text-align: center;
    font-size: 13px; color: var(--ink);
  }

  .section-head {
    position: absolute; left: 38px; width: 482px; height: 14px;
    display: flex; align-items: center; gap: 3px;
    font-size: 9.5px; text-transform: uppercase; color: var(--ink);
  }
  .section-head::before, .section-head::after {
    content: ""; flex: 1; border-top: 1px dashed var(--ink);
  }

  .col-label { position: absolute; font-size: 10px; }

  .item {
    position: absolute; left: 0; width: 100%; height: 14px; line-height: 14px;
    font-size: 10px;
  }
  .item .name { position: absolute; left: 61px; }
  .item .name::before {
    content: ""; position: absolute; left: -13px; top: 5px;
    width: 4px; height: 4px; border-radius: 50%; background: var(--ink);
  }
  .item.indent .name { left: 72px; }
  .item .price, .item .room { position: absolute; width: 60px; text-align: center; }
</style>
</head>
<body>

<section class="cover">
  <div class="cover-band">
    <h1 class="cover-title">Menu</h1>
    <div class="cover-rule top"></div>
    <div class="cover-name">VALMO</div>
    <div class="cover-rule bottom"></div>
  </div>
</section>

<section class="menu-page">
  <svg class="frame" width="572" height="812" viewBox="0 0 572 812" aria-hidden="true">
    <rect x="11" y="17" width="550" height="778" fill="none" stroke="#d4af3a" stroke-width="7"/>
    <path d="M31,190 Q75,190 75,162 L498,162 Q498,190 542,190 L542,737 Q498,737 498,766 L75,766 Q75,737 31,737 Z" fill="#d4af3a"/>
  </svg>
  <div class="ornament tl" role="img" aria-label="Volute décorative d'angle"></div>
  <div class="ornament tr" role="img" aria-label="Volute décorative d'angle"></div>
  <div class="ornament bl" role="img" aria-label="Volute décorative d'angle"></div>
  <div class="ornament br" role="img" aria-label="Volute décorative d'angle"></div>

  <div class="brand-pill">VALMO</div>
  <h2 class="page-title">Menu</h2>
  <p class="carte-title">Carte VALMO</p>

  <div class="section-head" style="top:275px">A partager ou pas</div>
  <span class="col-label" style="left:500px;top:297px">room</span>

  <div class="item" style="top:320px"><span class="name">Croque Miura jambon truffé &amp; Reblochon</span><span class="price" style="left:376px">14 €</span><span class="room" style="left:487px">19e</span></div>
  <div class="item" style="top:335px"><span class="name">Légumes cru, Houmous &amp; Cervelle de Canus</span><span class="price" style="left:376px">7 €</span><span class="room" style="left:487px">12e</span></div>
  <div class="item" style="top:350px"><span class="name">Rillettes de Sardines au beurre salé &amp; citron vert</span><span class="price" style="left:376px">7 €</span><span class="room" style="left:487px">12</span></div>
  <div class="item" style="top:365px"><span class="name">planche de Charcuterie de Savoie</span><span class="price" style="left:308px">petite 9 €</span><span class="price" style="left:376px">grande 14€</span><span class="room" style="left:465px">14 et 19</span></div>
  <div class="item" style="top:380px"><span class="name">Mozzarelle di buffala &amp; tomates cerise</span><span class="price" style="left:376px">11 €</span><span class="room" style="left:487px">16</span></div>
  <div class="item" style="top:395px"><span class="name">Truite Gravlax, pain taoster &amp; Crème cru</span><span class="price" style="left:376px">14 €</span><span class="room" style="left:487px">19</span></div>

  <div class="section-head" style="top:478px">Fromages</div>
  <div class="item indent" style="top:545px"><span class="name">Fromages de notre région, mesclun à l'huile de noisette</span><span class="price" style="left:422px">12e</span><span class="room" style="left:486px">17</span></div>
  <div class="item indent" style="top:568px"><span class="name">Faisselle sucre ou sale</span><span class="price" style="left:422px">7 e</span><span class="room" style="left:486px">9</span></div>

  <div class="section-head" style="top:614px">Desserts</div>
  <div class="item" style="top:660px"><span class="name">Tarte &nbsp;du jour</span><span class="price" style="left:420px">9 €</span><span class="room" style="left:487px">12</span></div>
  <div class="item" style="top:697px"><span class="name">Salade de fruits frais et financier</span><span class="price" style="left:420px">7 €</span><span class="room" style="left:487px">11</span></div>
  <div class="item" style="top:720px"><span class="name">Panna cotta coulis de fruits</span><span class="price" style="left:420px">7 e</span><span class="room" style="left:487px">11</span></div>
</section>

</body>
</html>
```